Web Developer Needs a Business Card Design

I need a personal business card design that represents me as a web developer for potential employers. I would like the background to be a dark color on the front for contrast with my logo and name. The back will have all my information along with a smaller version of the logo. I want something with a modern look and feel, not too conservative. This will be used for potential employers and freelance work.

Industry/Entity Type

Business

Contact Information for Business Card

Front should have my logo and name. The back should have all my personal information which would include: name: Tom Brevardi, phone: 570-614-9083, email: tombrevardi@mailwisp.com, website url: www.tombrevardi.com, logo, web developer.

Font styles to use
Sans Serif

Requirements
Must have
• Must include my logo. The color palette base color will be the logo color.

```html
<!DOCTYPE html>
<html lang="en">
<head>
<meta charset="utf-8">
<title>Tom Brevardi – Business Card</title>
<link rel="stylesheet" href="https://fonts.googleapis.com/css2?family=Nunito+Sans:wght@400&display=swap">
<style>
  :root {
    --page: #ffffff;
    --frame: #231f20;
    --ink-deep: #10061f;
    --ink-glow: #2e2440;
    --teal: #74d9c9;
    --mark-grey: #444446;
    --white: #ffffff;
  }
  * { margin: 0; padding: 0; box-sizing: border-box; }
  html, body {
    width: 1008px; height: 1200px; overflow: hidden;
    background: var(--page);
    font-family: "Nunito Sans", sans-serif;
  }
  .card {
    position: absolute; left: 165px; width: 675px; height: 377px;
    background: var(--frame); border-radius: 14px;
  }
  .card--front { top: 201px; }
  .card--back { top: 625px; }
  .card__face {
    position: absolute; left: 28px; top: 28px; right: 28px; bottom: 28px;
    overflow: hidden;
  }
  .card--front .card__face {
    background: linear-gradient(120deg, var(--ink-deep) 0%, var(--ink-deep) 48%, var(--ink-glow) 60%, var(--ink-glow) 82%, #1b1130 100%);
  }
  .card--back .card__face {
    background: linear-gradient(160deg, var(--ink-glow) 0%, var(--ink-glow) 30%, #170c28 62%, var(--ink-deep) 100%);
  }
  .front-mark {
    position: absolute; left: 167px; top: 117px; width: 86px; height: 86px;
  }
  .front-divider {
    position: absolute; left: 294px; top: 133px; width: 3px; height: 58px;
    background: var(--teal);
  }
  .front-name {
    position: absolute; left: 328px; top: 149px;
    font-size: 24px; line-height: 26px; font-weight: 400;
    color: var(--teal); letter-spacing: 0.2px;
  }
  .back-mark {
    position: absolute; left: -9px; top: -23px; width: 356px; height: 356px;
  }
  .back-details {
    position: absolute; left: 394px; top: 169px; color: var(--white);
  }
  .back-details__name { font-size: 22px; line-height: 22px; color: var(--teal); font-weight: 400; }
  .back-details__role { font-size: 13px; line-height: 13px; color: var(--teal); margin-top: 2px; }
  .back-details__contact {
    font-size: 17px; line-height: 20px; margin-top: 24px;
    font-style: normal; letter-spacing: -0.3px; white-space: nowrap;
  }
</style>
</head>
<body>
  <section class="card card--front">
    <div class="card__face">
      <svg class="front-mark" viewBox="0 0 86 86" aria-hidden="true">
        <circle cx="43" cy="43" r="39" fill="none" stroke="var(--teal)" stroke-width="5"/>
      </svg>
      <div class="front-divider"></div>
      <h1 class="front-name">TOM BREVARDI</h1>
    </div>
  </section>

  <section class="card card--back">
    <div class="card__face">
      <svg class="back-mark" viewBox="0 0 356 356" aria-hidden="true">
        <circle cx="178" cy="178" r="166" fill="none" stroke="var(--mark-grey)" stroke-width="12"/>
      </svg>
      <div class="back-details">
        <h2 class="back-details__name">TOM BREVARDI</h2>
        <p class="back-details__role">WEB DEVELOPER</p>
        <address class="back-details__contact">
          570-614-9083<br>
          tombrevardi@mailwisp.com<br>
          www.tombrevardi.com
        </address>
      </div>
    </div>
  </section>
</body>
</html>
```